TRV Mechanical Solutions Business Card Design

Business card design

Thinking just large logo on one side with a phone number and the back side is contact info with services we offer with a industrial plant across the bottom of the card

See must haves. I will be laser etching these business cards on black metal business cards as well as full color card stock. So must be bold and professional.

Target Market(s)

Industrial manufacturing

Contact Information for Business Card

Industrial manufacturing construction business specializing in consulting project managment and completing projects turn key

Font styles to use
Other font styles liked:
• See Logo for colors and font style

Requirements
Must have
• TRV Mechanical Solutions
• Gerald Munroe
• 2847 Alderwick Lane
• Bel Air, MD, 21047
• Project Managment
• Consulting
• Turn Key Industrial Projects
• I’d like a industrial manufacturing “cityline” on the back side bottom of the
• I’d like to be able to print these business cards in regular color on card stock but I’d also like the design to be etched into black metal business cards

```html
<!DOCTYPE html>
<html lang="en">
<head>
<meta charset="utf-8">
<title>TRV Mechanical Solutions – Business Card</title>
<link rel="stylesheet" href="https://fonts.googleapis.com/css2?family=Arimo:wght@400;700&display=swap">
<style>
  :root {
    --page-bg: #ececec;
    --card-bg: #333333;
    --card-text: #ececec;
    --card-muted: #d6d6d6;
    --band-dark: #474747;
    --band-light: #6a6a6a;
    --shadow: rgba(0, 0, 0, 0.25);
  }
  html, body {
    margin: 0;
    padding: 0;
    width: 1200px;
    height: 1000px;
    overflow: hidden;
    background: var(--page-bg);
    font-family: "Arimo", Arial, sans-serif;
  }
  .canvas {
    position: relative;
    width: 1200px;
    height: 1000px;
  }
  .card {
    position: absolute;
    background: var(--card-bg);
    color: var(--card-text);
    box-shadow: 0 4px 10px var(--shadow);
    overflow: hidden;
  }
  .card--front { left: 265px; top: 87px; width: 670px; height: 381px; }
  .card--back  { left: 263px; top: 523px; width: 672px; height: 384px; }

  .side-band {
    position: absolute;
    left: 13px;
    top: 0;
    width: 98px;
    height: 100%;
    background: linear-gradient(90deg, var(--band-dark) 0%, var(--band-dark) 50%, var(--band-light) 50%, var(--band-light) 100%);
  }

  .person-name {
    position: absolute;
    left: 169px;
    top: 64px;
    margin: 0;
    font-size: 30px;
    font-weight: 700;
    letter-spacing: 0.2px;
  }
  .person-title {
    position: absolute;
    left: 170px;
    top: 98px;
    margin: 0;
    font-size: 16px;
    color: var(--card-muted);
  }
  .contact-row {
    position: absolute;
    left: 168px;
    display: flex;
    align-items: flex-start;
    font-size: 16px;
    line-height: 17px;
    color: var(--card-muted);
  }
  .contact-row svg { width: 12px; height: 12px; margin-top: 4px; margin-right: 12px; fill: var(--card-muted); flex: none; }
  .contact-row--address { top: 144px; }
  .contact-row--address svg { margin-top: 6px; }
  .contact-row--phone { top: 189px; }
  .contact-row--phone svg { margin-top: 6px; }
  .contact-row--email { top: 220px; }
  .contact-row--email svg { margin-top: 7px; }
  .contact-row--web { top: 253px; }
  .contact-row--web svg { margin-top: 6px; }

  .services {
    position: absolute;
    left: 168px;
    top: 349px;
    margin: 0;
    font-size: 16.5px;
    color: var(--card-muted);
  }

  .brand-name {
    position: absolute;
    left: 0;
    right: 0;
    top: 172px;
    margin: 0;
    text-align: center;
    font-size: 30px;
    font-weight: 400;
    letter-spacing: 1px;
    color: var(--card-text);
  }
  .back-phone {
    position: absolute;
    left: 0;
    right: 0;
    top: 357px;
    display: flex;
    justify-content: center;
    align-items: center;
    font-size: 9px;
    font-weight: 700;
    color: var(--card-text);
  }
  .back-phone svg { width: 12px; height: 12px; margin-right: 5px; fill: var(--card-text); }
</style>
</head>
<body>
<div class="canvas">

  <section class="card card--front">
    <div class="side-band" role="img" aria-label="Vertical band of grey angled chevron pattern"></div>

    <h1 class="person-name">Gerald Munroe</h1>
    <p class="person-title">Director</p>

    <div class="contact-row contact-row--address">
      <svg viewBox="0 0 12 12" aria-hidden="true"><path d="M6 0a4 4 0 0 0-4 4c0 3 4 8 4 8s4-5 4-8a4 4 0 0 0-4-4zm0 5.6a1.6 1.6 0 1 1 0-3.2 1.6 1.6 0 0 1 0 3.2z"/></svg>
      <span>2847 Alderwick Lane<br>Bel Air, MD, 21047</span>
    </div>
    <div class="contact-row contact-row--phone">
      <svg viewBox="0 0 12 12" aria-hidden="true"><path d="M2.4 0.5l1.8 2.4-1 1.1c.7 1.6 1.9 2.8 3.5 3.6l1.1-1 2.4 1.8-.9 2c-4.8-.3-8.6-4.2-9-9l2.1-.9z"/></svg>
      <span>+61 200 555 010</span>
    </div>
    <div class="contact-row contact-row--email">
      <svg viewBox="0 0 12 12" aria-hidden="true"><path d="M0 2h12v1.2L6 6.6 0 3.2zM0 4.6l6 3.4 6-3.4V10H0z"/></svg>
      <span>info@trvmech.com</span>
    </div>
    <div class="contact-row contact-row--web">
      <svg viewBox="0 0 12 12" aria-hidden="true"><path d="M6 0a6 6 0 1 0 0 12A6 6 0 0 0 6 0zm4.6 5.3H8.5a9 9 0 0 0-.8-3.7 4.7 4.7 0 0 1 2.9 3.7zM6 1.3c.6.8 1.1 2.3 1.2 4H4.8c.1-1.7.6-3.2 1.2-4zM4.3 1.6a9 9 0 0 0-.8 3.7H1.4a4.7 4.7 0 0 1 2.9-3.7zM1.4 6.7h2.1a9 9 0 0 0 .8 3.7 4.7 4.7 0 0 1-2.9-3.7zM6 10.7c-.6-.8-1.1-2.3-1.2-4h2.4c-.1 1.7-.6 3.2-1.2 4zm1.7-.3a9 9 0 0 0 .8-3.7h2.1a4.7 4.7 0 0 1-2.9 3.7z"/></svg>
      <span>www.trvmech.com</span>
    </div>

    <p class="services">Project Managment | Consulting | Turn Key Industrial Projects</p>
  </section>

  <section class="card card--back">
    <h2 class="brand-name">TRV Mechanical Solutions</h2>
    <div class="back-phone">
      <svg viewBox="0 0 12 12" aria-hidden="true"><path d="M2.4 0.5l1.8 2.4-1 1.1c.7 1.6 1.9 2.8 3.5 3.6l1.1-1 2.4 1.8-.9 2c-4.8-.3-8.6-4.2-9-9l2.1-.9z"/></svg>
      <span>+61 200 555 010</span>
    </div>
  </section>

</div>
</body>
</html>
```